Single page 8 1/2 x 11 flyer to entice new homeowners to visit our WEBSITE

A single page flyer that we can put on an easel that promotes our website, tallowpine58.com, to new homeowners for blinds, shades, bath hardware, cabinet organization, etc. This piece will be on an easel in sales centers, design studios and closing offices. We want the homeowners to know where they can go to get reliable products and service from a trusted partner of their builder for products that were not installed in their new home before they closed.

Enter the coupon code KQT10 to get 10% off of your entire purchase and free shipping. The product on our website will put the finishing touches on their home. ....make your house your home

Target Market(s)

New homebuyers

Industry/Entity Type

Residential Construction

Font styles to use
Serif

Colors
ec1f27

Requirements
Must have
• Logo and website, tallowpine58.com and tagline, make your house your home
Nice to have
• what will drive new homeowners to the website to purchase items they did not purchase before closing like window blinds and shades, bath hardware, ceiling fans, grills, electric fireplaces, etc.

```html
<!DOCTYPE html>
<html lang="en">
<head>
<meta charset="utf-8">
<title>Tallow Pine 58 – Make Your House Your Home</title>
<link href="https://fonts.googleapis.com/css2?family=Oswald:wght@300;400;700&family=Roboto:wght@400;500;700&display=swap" rel="stylesheet">
<style>
  :root{
    --brand-red:#ec1f27;
    --ink:#1e1e1e;
    --grey:#8f8f8f;
    --grey-light:#c9c9c9;
    --paper:#ffffff;
    --panel:#f3f3f3;
    --backdrop:#e4e4e4;
  }
  html,body{margin:0;padding:0;width:1200px;height:1200px;overflow:hidden;background:var(--backdrop);}
  .flyer{position:absolute;left:160px;top:30px;width:880px;height:1139px;background:var(--paper);overflow:hidden;box-shadow:0 10px 30px rgba(0,0,0,.18);}
  .flyer-shapes{position:absolute;left:0;top:0;}
  .brand{position:absolute;left:48px;top:78px;display:flex;align-items:center;gap:14px;}
  .brand-dot{width:58px;height:58px;border-radius:50%;background:var(--brand-red);}
  .brand-name{font-family:'Oswald',sans-serif;font-weight:700;font-size:38px;color:var(--ink);letter-spacing:.5px;}
  .headline{position:absolute;left:48px;top:500px;margin:0;font-family:'Oswald',sans-serif;font-weight:300;font-size:64px;color:var(--ink);letter-spacing:-1px;white-space:nowrap;}
  .headline strong{font-weight:700;color:var(--brand-red);}
  .section-title{font-family:'Roboto',sans-serif;font-weight:700;color:var(--brand-red);font-size:24px;margin:0;}
  .products{position:absolute;left:48px;top:630px;}
  .product-list{display:flex;gap:34px;margin-top:14px;font-family:'Roboto',sans-serif;font-size:17px;color:var(--ink);}
  .product-list ul{list-style:none;margin:0;padding:0;}
  .product-list li{position:relative;padding-left:14px;margin-bottom:8px;line-height:1.15;max-width:170px;}
  .product-list li::before{content:"";position:absolute;left:0;top:7px;width:5px;height:5px;border-radius:50%;background:var(--brand-red);}
  .contact{position:absolute;left:48px;top:790px;font-family:'Roboto',sans-serif;}
  .contact-label{font-weight:700;color:var(--brand-red);font-size:24px;margin:0;}
  .contact-value{font-weight:700;color:var(--ink);font-size:30px;margin:2px 0 22px 6px;}
  .social{display:flex;gap:16px;margin-left:14px;}
  .social span{width:34px;height:34px;border-radius:6px;background:var(--grey);}
  .badge{position:absolute;border-radius:50%;background:var(--paper);display:flex;flex-direction:column;align-items:center;justify-content:center;font-family:'Oswald',sans-serif;text-align:center;line-height:.95;}
  .badge-discount{left:590px;top:600px;width:240px;height:240px;}
  .badge-discount .big{font-weight:700;color:var(--brand-red);font-size:92px;}
  .badge-discount .small{font-weight:400;color:var(--ink);font-size:30px;}
  .badge-shipping{left:415px;top:795px;width:170px;height:170px;}
  .badge-shipping .big{font-weight:700;color:var(--brand-red);font-size:54px;}
  .badge-shipping .small{font-weight:400;color:var(--ink);font-size:30px;}
</style>
</head>
<body>
<div class="flyer">
  <svg class="flyer-shapes" width="880" height="1139" viewBox="0 0 880 1139">
    <defs>
      <linearGradient id="roomTone" x1="0" y1="0" x2="1" y2="1">
        <stop offset="0" stop-color="#7a7772"/>
        <stop offset=".45" stop-color="#d9d2c4"/>
        <stop offset="1" stop-color="#b9b1a5"/>
      </linearGradient>
    </defs>
    <rect x="0" y="462" width="880" height="600" fill="var(--panel)"/>
    <polygon points="585,0 880,0 880,430 60,430" fill="url(#roomTone)" role="img" aria-label="Bright living room with fireplace, ceiling fan, window shades and white sofa"/>
    <polygon points="48,430 560,0 585,0 72,430" fill="var(--brand-red)"/>
    <polygon points="20,430 530,0 548,0 38,430" fill="var(--ink)"/>
    <polygon points="430,70 880,260 880,272 430,82" fill="var(--brand-red)" opacity=".8"/>
    <polygon points="0,438 880,438 880,466 0,470" fill="var(--brand-red)"/>
    <rect x="0" y="470" width="880" height="4" fill="var(--ink)"/>
    <polygon points="880,520 880,545 345,1062 315,1062" fill="var(--grey)"/>
    <polygon points="880,560 880,650 440,1062 330,1062" fill="var(--brand-red)"/>
    <circle cx="710" cy="720" r="128" fill="none" stroke="var(--grey-light)" stroke-width="16"/>
    <path d="M710 592 A128 128 0 0 1 710 848" fill="none" stroke="var(--brand-red)" stroke-width="16"/>
    <circle cx="500" cy="880" r="92" fill="none" stroke="var(--grey-light)" stroke-width="12"/>
    <path d="M500 788 A92 92 0 0 1 500 972" fill="none" stroke="var(--brand-red)" stroke-width="12"/>
    <rect x="0" y="1062" width="880" height="6" fill="var(--paper)"/>
    <rect x="0" y="1068" width="880" height="71" fill="var(--brand-red)"/>
  </svg>

  <div class="brand">
    <span class="brand-dot"></span>
    <span class="brand-name">TALLOW PINE 58</span>
  </div>

  <h1 class="headline">MAKE YOUR HOUSE <strong>YOUR HOME</strong></h1>

  <div class="products">
    <h2 class="section-title">Purchase Items</h2>
    <div class="product-list">
      <ul><li>Window blinds and shades</li><li>Bath hardware</li></ul>
      <ul><li>Ceiling fans</li><li>Grills</li></ul>
      <ul><li>Electric fireplaces</li><li>Cabinet Hardware</li></ul>
    </div>
  </div>

  <div class="contact">
    <p class="contact-label">Call us:</p>
    <p class="contact-value">(555)240-1187</p>
    <p class="contact-label">Visit us online:</p>
    <p class="contact-value">tallowpine58.com</p>
    <div class="social"><span></span><span></span><span></span></div>
  </div>

  <div class="badge badge-discount"><span class="big">10%</span><span class="small">OFF DISCOUNT</span></div>
  <div class="badge badge-shipping"><span class="big">FREE</span><span class="small">SHIPPING</span></div>
</div>
</body>
</html>
```